VelloPath Business Card

Our company is called VelloPath and we are based in Tel Aviv, Israel. We create innovative and exciting methods for getting people on the web engaged with content. We need a cool yet professional business card that will represent our management level employees. keep in mind this is a start up company with a young atmosphere. You can be inspired by our logo (file attached, make sure you have the right font "Ubuntu-Condensed") Use the colors that are used in the logo and create a colourful and professional business card.

```html
<!DOCTYPE html>
<html lang="en">
<head>
<meta charset="utf-8">
<title>VelloPath Business Card</title>
<link rel="stylesheet" href="https://fonts.googleapis.com/css2?family=Ubuntu+Condensed&display=swap">
<style>
  :root {
    --backdrop: #1c1c1c;
    --card-base: #3a3a3a;
    --dot-pink: #e8207a;
    --dot-yellow: #fecb0a;
    --dot-blue: #4fb3e0;
    --dot-purple: #8e2b8f;
    --dot-green: #84c441;
    --dot-orange: #f7a940;
    --wordmark: #ffffff;
  }
  * { margin: 0; padding: 0; box-sizing: border-box; }
  html, body {
    width: 1200px;
    height: 800px;
    overflow: hidden;
    background: var(--backdrop);
  }
  .sheet {
    position: relative;
    width: 1200px;
    height: 800px;
  }
  .card {
    position: absolute;
    width: 480px;
    height: 273px;
    border-radius: 18px;
    overflow: hidden;
    background: var(--card-base);
  }
  .card--top-left { left: 100px; top: 88px; }
  .card--top-right { left: 624px; top: 88px; }
  .card--bottom-left { left: 100px; top: 437px; }
  .card--bottom-right { left: 624px; top: 437px; }

  .card__pattern {
    position: absolute;
    inset: 0;
    background:
      radial-gradient(circle at 20% 30%, rgba(232, 32, 122, 0.35), transparent 45%),
      radial-gradient(circle at 75% 40%, rgba(254, 203, 10, 0.30), transparent 45%),
      radial-gradient(circle at 45% 80%, rgba(79, 179, 224, 0.30), transparent 45%),
      radial-gradient(circle at 85% 85%, rgba(132, 196, 65, 0.25), transparent 40%),
      radial-gradient(circle at 10% 85%, rgba(247, 169, 64, 0.25), transparent 40%),
      var(--card-base);
  }
  .card__wordmark {
    position: absolute;
    font-family: "Ubuntu Condensed", "Arial Narrow", sans-serif;
    font-size: 56px;
    line-height: 1;
    color: var(--wordmark);
    letter-spacing: 0.5px;
  }
  .card--top-left .card__wordmark { left: 40px; top: 30px; }
  .card--top-right .card__wordmark { right: 46px; top: 30px; }
  .card--bottom-left .card__wordmark { left: 40px; bottom: 24px; }
  .card--bottom-right .card__wordmark { right: 100px; bottom: 24px; }
</style>
</head>
<body>
<main class="sheet">
  <section class="card card--top-left">
    <div class="card__pattern" role="img" aria-label="Colourful polka dot pattern in pink, yellow, blue, purple, green and orange on charcoal"></div>
    <p class="card__wordmark">VelloPath</p>
  </section>
  <section class="card card--top-right">
    <div class="card__pattern" role="img" aria-label="Colourful polka dot pattern in pink, yellow, blue, purple, green and orange on charcoal"></div>
    <p class="card__wordmark">VelloPath</p>
  </section>
  <section class="card card--bottom-left">
    <div class="card__pattern" role="img" aria-label="Colourful polka dot pattern in pink, yellow, blue, purple, green and orange on charcoal"></div>
    <p class="card__wordmark">VelloPath</p>
  </section>
  <section class="card card--bottom-right">
    <div class="card__pattern" role="img" aria-label="Colourful polka dot pattern in pink, yellow, blue, purple, green and orange on charcoal"></div>
    <p class="card__wordmark">VelloPath</p>
  </section>
</main>
</body>
</html>
```